Business Card Design

We are a business based in Sydney repairing and restoring timber windows. We mainly cater to residential home owners although sometimes work with larger building companies. We do a lot of work in heritage buildings though also cater to modern windows.
Our Logo is Black and Gold and were thinking of using a white card with only these two colours although we are open to any design suggestions. Check out our website for ideas.
Front of Card
Contact Information, Website & Business Name
Back of Card
Business Logo, website?
Target Market(s)
Home Owners
Industry/Entity Type
Residential
Contact Information for Business Card
Casement Craft Renewals
Owen Castell
0457 302 689
owen@casementcraftrenewals.com
www.casementcraftrenewals.com
Look and feel

```html
<!DOCTYPE html>
<html lang="en">
<head>
<meta charset="utf-8">
<title>Casement Craft Renewals – Business Card</title>
<link href="https://fonts.googleapis.com/css2?family=Lato:wght@400;700;900&display=swap" rel="stylesheet">
<style>
  :root {
    --ink: #1d1d1b;
    --paper: #ffffff;
    --gold: #d4a51c;
    --gold-deep: #7a5410;
    --gold-mid: #b07d14;
    --backdrop: #2b2b2b;
  }
  * { box-sizing: border-box; margin: 0; padding: 0; }
  html, body { width: 1200px; height: 900px; overflow: hidden; }
  body {
    background: var(--backdrop);
    font-family: "Lato", sans-serif;
    color: var(--ink);
    position: relative;
  }
  .card {
    position: absolute;
    width: 560px;
    height: 320px;
    background: var(--paper);
    overflow: hidden;
  }
  .card-back { left: 70px; top: 100px; }
  .card-front { left: 570px; top: 480px; }

  .card-band { position: absolute; inset: 0; width: 100%; height: 100%; }

  .brand-name {
    position: absolute;
    font-weight: 400;
    color: var(--ink);
    line-height: 1.05;
    letter-spacing: 0.5px;
  }
  .card-back .brand-name { left: 110px; top: 70px; font-size: 40px; }
  .card-front .brand-name { left: 70px; top: 56px; font-size: 32px; }

  .website-line {
    position: absolute;
    left: 120px;
    bottom: 30px;
    font-size: 15px;
    font-weight: 700;
    letter-spacing: 4.2px;
    color: #333;
  }

  .person {
    position: absolute;
    right: 26px;
    top: 22px;
    text-align: right;
  }
  .person-name {
    font-size: 19px;
    font-weight: 900;
    color: var(--gold-mid);
    letter-spacing: 0.3px;
  }
  .person-role {
    font-size: 12px;
    font-weight: 700;
    letter-spacing: 0.6px;
    color: var(--ink);
    margin-top: -2px;
  }

  .services {
    position: absolute;
    right: 26px;
    top: 158px;
    text-align: right;
    font-size: 13.5px;
    font-weight: 700;
    line-height: 1.35;
    white-space: nowrap;
  }

  .contact-tab {
    position: absolute;
    left: 0;
    top: 190px;
    width: 44px;
    height: 108px;
    background: linear-gradient(180deg, var(--gold-mid), var(--gold));
    border-radius: 0 10px 10px 0;
    display: flex;
    flex-direction: column;
    align-items: center;
    justify-content: space-around;
    padding: 8px 0;
  }
  .contact-tab svg { width: 20px; height: 20px; }

  .contact-list {
    position: absolute;
    left: 58px;
    top: 192px;
    list-style: none;
    font-size: 13px;
    font-weight: 700;
    line-height: 1.25;
  }
  .contact-list li { margin-bottom: 9px; }
  .contact-list li:last-child { margin-bottom: 0; }
</style>
</head>
<body>

  <section class="card card-back" aria-label="Business card back">
    <svg class="card-band" viewBox="0 0 560 320" preserveAspectRatio="none" aria-hidden="true">
      <path d="M330 320 Q340 300 365 298 L560 296 L560 320 Z" fill="var(--gold-deep)" opacity="0.85"/>
      <path d="M560 290 L560 298 L370 298 Q350 299 340 310 Q352 292 372 290 Z" fill="var(--gold)"/>
    </svg>
    <div class="brand-name">Casement<br>Craft<br>Renewals</div>
    <div class="website-line">www.casementcraftrenewals.com</div>
  </section>

  <section class="card card-front" aria-label="Business card front">
    <svg class="card-band" viewBox="0 0 560 320" preserveAspectRatio="none" aria-hidden="true">
      <path d="M380 320 Q392 300 418 298 L560 296 L560 320 Z" fill="var(--gold-deep)" opacity="0.85"/>
      <path d="M560 290 L560 298 L420 298 Q398 299 388 310 Q400 292 422 290 Z" fill="var(--gold)"/>
    </svg>

    <div class="person">
      <div class="person-name">OWEN CASTELL</div>
      <div class="person-role">DIRECTOR</div>
    </div>

    <div class="brand-name">Casement<br>Craft<br>Renewals</div>

    <p class="services">Rot Repairs, Sash Cords,<br>Glazing, Double Glazing,<br>Spiral Balancers (springs)<br>&amp; much more</p>

    <div class="contact-tab" aria-hidden="true">
      <svg viewBox="0 0 20 20"><rect x="5" y="1.5" width="10" height="17" rx="2" fill="none" stroke="#fff" stroke-width="1.6"/><line x1="8.5" y1="15.5" x2="11.5" y2="15.5" stroke="#fff" stroke-width="1.4"/></svg>
      <svg viewBox="0 0 20 20"><rect x="2" y="4.5" width="16" height="11" fill="none" stroke="#fff" stroke-width="1.6"/><path d="M2 4.5 L10 11 L18 4.5" fill="none" stroke="#fff" stroke-width="1.6"/></svg>
      <svg viewBox="0 0 20 20"><path d="M10 19 C5 13 4 10 4 8 A6 6 0 0 1 16 8 C16 10 15 13 10 19 Z" fill="#fff"/><circle cx="10" cy="8" r="2.3" fill="var(--gold)"/></svg>
    </div>

    <ul class="contact-list">
      <li>0457 302 689<br>www.casementcraftrenewals.com</li>
      <li>owen@casementcraftrenewals.com</li>
      <li>Harlow Vale 2140, Upper Ridge Suburbs<br>Kestrel Point &amp; Bayside Coast</li>
    </ul>
  </section>

</body>
</html>
```